The Quiet Ascent Book Cover

Book Title:
The Quiet Ascent: Lessons of Insight From A Circle of Mentors to Guide You Toward a Fuller Journey

This book will offer the wisdom and philosophies of a variety of different coaches to allow future clients to get a taste of you and your style and prepare them to work with you!

A coach does not fix you. Or heal you. They coach you - offer thoughts to ponder, guidance, techniques to try. All to help you plays and succeed at the game of life.

Each coach has their own personality, training, experience, method and philosophy they bring to the table. The underlying purpose is to guide you through The Quiet Ascent, to become the person you desire and aspire to be. Different coaches for different folks, yet they all have their own unique wisdom and special sauce to share.

This book is a collection of just that. A tasting of the wisdom and philosophies of a variety of different coaches for you to experience.

Types of Coaches: Clarity, Dreams, Goals, Motivation, Mindset,  Subconscious, Beliefs, Behavior, Accountability, Life, Wellness, Love & Dating, Relationships, Sex, Business, Career,  Executive,  Personal Development,  Writing, Wellness, Fitness, Parenting,  Style, Spirituality, Public Speaking, Financial,  Time management, Weight Loss, Running, Self esteem,  Tarot, Astrology, Enneagram, Soul path/ Dharma, Skills, Performance,  Speaking / Communication, Leadership, Shadow Work, Acting, Sports, ANY & ALL

Target Market(s)

Males or females looking for guidance and words of wisdom from an expert coach - maybe to find one that resonates with them to work with further. Ages 16 and up. Any Gender. International. Looking to improve their life!

Industry/Entity Type

Self Development, Wellness, Coaching, Personal Growth, Fitness, Spirituality, Business, Relationships

Font styles to use
Serif
Script

Colors
0054AA
0677BA
7BADD7
CADEEF
E8F1F8
FFF300
FFF600
FEFA6F
FFFEC7
FFFEE8

Requirements
Must have
• I am looking for a visually appealing, unique cover that encompasses the breadth and depth of the transformation that people can go through and inspires them to want to grow and change even more. I love when elegant and classic simplicity is combined with some kind of twist that catches the eye and provokes thought. I love complimentary fonts, colors, design elements. You can visit my Veltrano Author Page - Dr. Marisol Penbury Aldane to see my titles to see what I have liked! But I am also excited to see where you can make my vision even better!!
Nice to have
• Front Cover - Image, Title and Subtitle, The Lark Publishing House, Spine - Title and Publishing House Logo, Back - Book Blurb, Authors Names, Info about Publishing House, ISBN Barcode
Should not have
• Anything too feminine or too masculine as I want to encourage coaches of all genders to participate.

```html
<!DOCTYPE html>
<html lang="en">
<head>
<meta charset="utf-8">
<title>The Quiet Ascent — Book Cover</title>
<link href="https://fonts.googleapis.com/css2?family=Roboto:wght@400;500&family=Oswald:wght@700&family=Kaushan+Script&display=swap" rel="stylesheet">
<style>
  :root{
    --canvas:#f2f2f2;
    --back-blue:#0a6ba6;
    --spine-navy:#0d3f63;
    --title-blue:#0a74bf;
    --accent-orange:#e6a54a;
    --ink-white:#ffffff;
    --line-aqua:#7fd0ea;
    --photo-blue:#0c5a8c;
    --figure-deep:#0e5d93;
    --figure-light:#6fb7e0;
  }
  *{margin:0;padding:0;box-sizing:border-box}
  html,body{width:1200px;height:900px;overflow:hidden}
  body{background:var(--canvas);position:relative;font-family:"Roboto",Arial,sans-serif}

  .back-cover,.spine,.front-cover{position:absolute;top:137px;height:648px;box-shadow:0 2px 8px rgba(0,0,0,.18);overflow:hidden}
  .back-cover{left:115px;width:432px;background:var(--back-blue);color:var(--ink-white)}
  .spine{left:582px;width:40px;background:var(--spine-navy)}
  .front-cover{left:652px;width:432px;background:linear-gradient(135deg,#ffffff 55%,#f1f1f1)}

  /* back */
  .author-photo{position:absolute;left:27px;top:54px;width:146px;height:146px;border-radius:50%;border:3px solid var(--ink-white);background:linear-gradient(160deg,#1a6fa3,var(--photo-blue) 60%,#0a4c78)}
  .bio-rule{position:absolute;left:187px;top:53px;width:2px;height:161px;background:var(--ink-white)}
  .bio{position:absolute;left:195px;top:54px;width:228px;font-size:7.3px;line-height:9.2px}
  .about-heading{position:absolute;left:24px;top:272px;font-family:"Kaushan Script",cursive;font-weight:400;font-size:30px;color:var(--ink-white)}
  .blurb{position:absolute;left:27px;top:343px;width:392px;font-size:7.6px;line-height:9.1px}
  .blurb p{margin-bottom:9px}
  .back-divider{position:absolute;left:29px;top:485px;width:383px;height:1px;background:var(--line-aqua)}
  .publisher-label{position:absolute;left:27px;top:544px;font-size:7px;letter-spacing:3.2px}
  .publisher-about{position:absolute;left:25px;top:558px;width:176px;font-size:6.3px;line-height:9.1px}
  .isbn-box{position:absolute;left:224px;top:542px;width:161px;height:100px;background:#f8f8f8}

  /* spine */
  .spine-publisher{position:absolute;top:8px;left:0;width:40px;height:262px;writing-mode:vertical-rl;transform:rotate(180deg);display:flex;align-items:center;justify-content:flex-end;white-space:nowrap;color:var(--ink-white);font-size:10.5px;letter-spacing:3.9px}
  .spine-title{position:absolute;bottom:16px;left:0;width:40px;writing-mode:vertical-rl;transform:rotate(180deg);display:flex;align-items:center;white-space:nowrap;color:var(--ink-white);font-family:"Oswald",sans-serif;font-weight:700;font-size:27px;line-height:1}
  .spine-title .script{font-family:"Kaushan Script",cursive;font-weight:400;color:var(--accent-orange);font-size:24px;margin-top:10px}

  /* front */
  .front-author{position:absolute;top:15px;width:100%;text-align:center;color:var(--accent-orange);font-size:13px}
  .front-title{position:absolute;top:40px;width:100%;text-align:center;color:var(--title-blue);font-family:"Oswald",sans-serif;font-weight:700;font-size:28px;line-height:1.2}
  .front-script{position:absolute;top:68px;width:100%;text-align:center;color:var(--accent-orange);font-family:"Kaushan Script",cursive;font-weight:400;font-size:72px;line-height:1.1}
  .figure-art{position:absolute;left:135px;top:150px;width:140px;height:446px;border-radius:70px 70px 40px 40px;background:linear-gradient(180deg,var(--figure-deep) 0%,var(--figure-light) 40%,#f0d27a 52%,var(--figure-light) 60%,var(--figure-deep) 100%);opacity:.9}
  .front-subtitle{position:absolute;top:600px;width:100%;text-align:center;color:var(--title-blue);font-size:9.5px;line-height:13px;letter-spacing:.7px;font-weight:500}
  .front-subtitle .hl{color:var(--accent-orange)}
  .front-band{position:absolute;left:0;bottom:0;width:100%;height:20px;background:var(--back-blue);color:var(--ink-white);font-size:16px;letter-spacing:7.6px;text-align:center;line-height:21px}
</style>
</head>
<body>

<section class="back-cover">
  <div class="author-photo" role="img" aria-label="Circular portrait photograph of the author"></div>
  <div class="bio-rule"></div>
  <p class="bio">Dr. Mari Penbury Aldane is a Doctor of Physical Therapy, Owner of The Lark Wellness Studio and The Lark Publishing House, a Holistic Life Transformation Coach, and International Bestselling Author. Decades of professional experience with patients, students, and clients makes her coaching effective, efficient, and easily integrated into your life. Her passion is to support the well-being and healing of your heart, mind, body, and soul as you learn to love your authentic self. Mari will empower you to become the author of your own life story as you discover unconsidered possibilities, remove barriers to success and unlock your full potential to live a creative life you love. Her own personal life journey prepared her to use her voice to amplify the voices of others to create even more impact in the world. You can find her enjoying living her best life as a mom of three divine masculine men in the making and expanding her own potential as a perfectly imperfect human being.</p>

  <h2 class="about-heading">About the Book</h2>
  <div class="blurb">
    <p>This book will offer the wisdom and philosophies of a variety of different coaches to allow future clients to get a taste of you and your style and prepare them to work with you!</p>
    <p>A coach does not fix you. Or heal you. They coach you - offer thoughts to ponder, guidance, techniques to try. All to help you plays and succeed at the game of life.</p>
    <p>Each coach has their own personality, training, experience, method and philosophy they bring to the table. The underlying purpose is to guide you through The Quiet Ascent, to become the person you desire and aspire to be. Different coaches for different folks, yet they all have their own unique wisdom and special sauce to share.</p>
    <p>This book is a collection of just that. A tasting of the wisdom and philosophies of a variety of different coaches for you to experience.</p>
  </div>
  <div class="back-divider"></div>

  <div class="publisher-label">THE LARK PUBLISHING HOUSE</div>
  <p class="publisher-about">Contrary to popular belief, Lorem Ipsum is not simply random text. It has roots in a piece of classical Latin literature from 45 BC, making it over 2000 years old. Edwin Harrowgate, a Latin professor at Mossvale College in Ardenshire, looked up one of the more obscure Latin words, consectetur, from a Lorem Ipsum passage, and going through the cites of the word in classical literature, discovered the undoubtable source.</p>
  <div class="isbn-box"></div>
</section>

<section class="spine">
  <div class="spine-publisher">THE LARK PUBLISHING HOUSE</div>
  <div class="spine-title"><span>The Quiet</span><span class="script">Ascent</span></div>
</section>

<section class="front-cover">
  <div class="front-author">Dr. Marisol Penbury Aldane</div>
  <h1 class="front-title">The Quiet</h1>
  <div class="front-script">Ascent</div>
  <div class="figure-art" role="img" aria-label="Illustration of a person in a tree yoga pose formed from many blue and yellow butterflies"></div>
  <p class="front-subtitle">LESSONS OF <span class="hl">INSIGHT</span> FROM A CIRCLE OF<br>MENTORS TO GUIDE YOU TOWARD A <span class="hl">FULLER JOURNEY</span></p>
  <div class="front-band">THE LARK PUBLISHING HOUSE</div>
</section>

</body>
</html>
```